Need a website for our company

We need a website for our company to showcase all our work for customers to see.
We do all phases of home improvement:
Dormers/Extensions
Basement Remodel
Masonry/Concrete/Pavers/Asphalt
Cultured Stone Veneer
Kitchens
Bathrooms
Pool designs
Outdoor Bathroom
Outdoor Kitchens
Tile work
For reference, something similar to this website: https://brightlanebuilders.example/
Target Market(s)
We are trying to target homeowners.
Coding
Coded - Design and coding required
Number of Pages Required
5+ page
Look and feel

```html
<!DOCTYPE html>
<html lang="en">
<head>
<meta charset="utf-8">
<title>Harlow &amp; Sons Construction Inc — Family Home Improvement</title>
<link rel="stylesheet" href="https://fonts.googleapis.com/css2?family=Bebas+Neue&family=Poppins:wght@400;500;600&display=swap">
<style>
:root{
  --dark:#333333;
  --darker:#2b2b2b;
  --ink:#222222;
  --muted:#7a7a7a;
  --line:#e6e6e6;
  --white:#ffffff;
  --gray:#6b6b6b;
}
*{box-sizing:border-box;margin:0;padding:0}
html,body{width:1200px;height:4275px;overflow:hidden}
body{position:relative;background:var(--white);font-family:"Poppins",sans-serif;color:var(--ink)}
.heading{font-family:"Bebas Neue",sans-serif;color:var(--darker);letter-spacing:1px;font-weight:400}
.section-title{position:absolute;left:0;width:1200px;text-align:center;font-size:46px}
.body-text{font-size:13px;line-height:22px;color:var(--muted)}

/* header */
.site-header{position:absolute;left:0;top:0;width:1200px;height:95px;background:var(--white);z-index:5}
.brand{position:absolute;left:88px;top:24px;display:flex;align-items:center;gap:8px}
.brand-mark{width:14px;height:14px;background:var(--dark)}
.brand-name{font-size:10px;font-weight:600;color:var(--dark);letter-spacing:.5px;white-space:nowrap}
.brand-tag{position:absolute;left:88px;top:48px;font-size:7px;color:var(--muted);letter-spacing:1.5px;white-space:nowrap}
.main-nav{position:absolute;left:379px;top:39px;display:flex;gap:20px;font-size:12.5px;color:#555;white-space:nowrap}
.main-nav .active{color:var(--ink);font-weight:600;position:relative}
.main-nav .active::before{content:"";position:absolute;left:0;right:0;top:-39px;height:2px;background:var(--dark)}
.call-btn{position:absolute;left:901px;top:27px;width:210px;height:43px;background:var(--dark);color:var(--white);font-size:12.5px;font-weight:600;display:flex;align-items:center;white-space:nowrap}
.call-btn .ico{width:40px;height:43px;background:#444;display:flex;align-items:center;justify-content:center;margin-right:12px}

/* hero */
.hero-photo{position:absolute;left:0;top:95px;width:1200px;height:905px;background:linear-gradient(110deg,#6d6a66 0%,#8f8a83 35%,#a7a29a 60%,#5a5450 100%)}
.hero-curve{position:absolute;left:0;top:600px;width:1200px;height:420px}
.hero-title{position:absolute;left:86px;top:312px;font-size:90px;line-height:80px;color:var(--white)}
.hero-text{position:absolute;left:88px;top:490px;width:430px;font-size:13.5px;line-height:22px;color:var(--white)}
.btn-light{position:absolute;left:88px;top:551px;width:139px;height:44px;background:var(--white);color:var(--ink);font-size:12px;font-weight:600;display:flex;align-items:center;justify-content:center}

/* services */
.service-card{position:absolute;top:977px;width:301px;height:348px;background:var(--white);box-shadow:0 4px 16px rgba(0,0,0,.08)}
.service-photo{width:301px;height:263px}
.service-label{height:85px;display:flex;align-items:center;justify-content:center;gap:12px;font-size:20px}
.dots{position:absolute;display:flex;gap:8px;align-items:center}
.dots i{width:10px;height:10px;border-radius:50%;background:#aaa;display:block}
.dots i.on{width:13px;height:13px;background:var(--dark)}

/* about */
.about-photo{position:absolute;left:0;top:1416px;width:537px;height:530px;background:linear-gradient(160deg,#5b4a3a,#a6784e 50%,#3b2d22)}
.play{position:absolute;left:88px;top:1901px;width:92px;height:92px;border-radius:50%;background:#555;display:flex;align-items:center;justify-content:center}
.about-title{position:absolute;left:591px;top:1498px;font-size:46px}
.about-text{position:absolute;left:591px;top:1555px;width:500px}
.btn-dark{position:absolute;left:592px;top:1797px;width:141px;height:44px;background:var(--dark);color:var(--white);font-size:12px;font-weight:600;display:flex;align-items:center;justify-content:center}

/* select */
.tip{position:absolute;width:260px}
.tip svg{display:block;height:64px}
.tip h3{font-size:19px;margin-top:30px;white-space:nowrap}
.tip p{margin-top:6px}

/* portfolio */
.folio{position:absolute;top:2660px;height:345px}

/* testimonials */
.quote-card{position:absolute;top:3236px;width:335px;height:234px;background:var(--white);box-shadow:0 4px 18px rgba(0,0,0,.07)}
.quote-card .q{position:absolute;right:95px;top:20px;font-family:"Bebas Neue",sans-serif;font-size:180px;line-height:180px;color:#f0f0f0}
.quote-card p{position:absolute;left:25px;top:90px;width:290px}
.quote-card h4{position:absolute;left:25px;top:186px;font-size:18px}
.avatar{position:absolute;top:3186px;width:92px;height:92px;border-radius:50%}

/* footer */
.footer-band{position:absolute;left:0;top:3520px;width:1200px;height:755px;background:var(--dark)}
.footer-curve{position:absolute;left:0;top:3500px;width:1200px;height:300px}
.news-title{position:absolute;left:0;top:3825px;width:1200px;text-align:center;color:var(--white);font-size:46px}
.news-form{position:absolute;left:310px;top:3885px;width:579px;height:45px;background:var(--white);display:flex;border:2px solid var(--white)}
.news-form span{flex:1;font-size:12.5px;color:#444;padding-left:16px;line-height:41px}
.news-form b{width:123px;background:var(--dark);color:var(--white);font-size:12px;font-weight:600;text-align:center;line-height:41px}
.foot-brand{position:absolute;left:100px;top:4040px;width:360px;text-align:center}
.foot-brand .mark{width:26px;height:26px;background:var(--white);margin:0 auto 16px}
.foot-brand .name{color:var(--white);font-size:14px;font-weight:600;letter-spacing:1.2px;white-space:nowrap}
.foot-brand .tag{color:#bbb;font-size:9px;letter-spacing:3px;margin-top:4px;white-space:nowrap}
.socials{position:absolute;left:209px;top:4153px;display:flex;gap:11px}
.socials i{display:block;width:25px;height:25px;border-radius:50%;background:#4a4a4a;border:1px solid #5c5c5c}
.foot-col{position:absolute;top:4008px;color:var(--white)}
.foot-col h5{font-family:"Bebas Neue",sans-serif;font-weight:400;font-size:25px;letter-spacing:1px;margin-bottom:16px}
.foot-col li{list-style:none;font-size:12px;line-height:20.5px;color:#e6e6e6;white-space:nowrap}
.contact-item{display:flex;gap:6px;font-size:12px;line-height:16px;color:#e6e6e6;margin-bottom:8px;white-space:nowrap}
.contact-item svg{flex:none;margin-top:2px}
.foot-rule{position:absolute;left:88px;top:4240px;width:1024px;height:1px;background:#555}
.to-top{position:absolute;left:1115px;top:4222px;width:38px;height:38px;border-radius:50%;background:#4a4a4a;display:flex;align-items:center;justify-content:center}
.copyright{position:absolute;left:0;top:4251px;width:1200px;text-align:center;font-family:"Bebas Neue",sans-serif;font-size:15px;color:var(--white);letter-spacing:.5px}
</style>
</head>
<body>

<header class="site-header">
  <div class="brand"><span class="brand-mark"></span><span class="brand-name">HARLOW &amp; SONS CONSTRUCTION INC</span></div>
  <div class="brand-tag">WE TREAT OUR CUSTOMERS LIKE FAMILY</div>
  <nav class="main-nav">
    <span class="active">HOME</span><span>ABOUT US</span><span>SELECTING A COMPANY</span><span>OUR WORK</span><span>CONTACT US</span>
  </nav>
  <div class="call-btn"><span class="ico"><svg width="16" height="16" viewBox="0 0 24 24"><path fill="#fff" d="M6.6 10.8a15.1 15.1 0 006.6 6.6l2.2-2.2c.3-.3.7-.4 1-.2 1.1.4 2.3.6 3.6.6.6 0 1 .4 1 1V20c0 .6-.4 1-1 1A17 17 0 013 4c0-.6.4-1 1-1h3.5c.6 0 1 .4 1 1 0 1.3.2 2.5.6 3.6.1.3 0 .7-.2 1l-2.3 2.2z"/></svg></span>CALL US: 0100 555 010</div>
</header>

<section class="hero">
  <div class="hero-photo" role="img" aria-label="Two builders measuring and marking timber on a workbench in a home under renovation"></div>
  <svg class="hero-curve" viewBox="0 0 1200 420" preserveAspectRatio="none" aria-hidden="true">
    <path d="M0 395 C 260 200 520 110 760 120 C 960 128 1110 215 1200 300 L1200 420 L0 420 Z" fill="#333"/>
    <path d="M0 395 C 260 210 520 130 760 140 C 960 150 1100 230 1200 330 L1200 420 L0 420 Z" fill="#fff"/>
  </svg>
  <h1 class="heading hero-title">FAMILY HOME<br>IMPROVEMENT</h1>
  <p class="hero-text">There are many variations of passages of Lorem Ipsum available, but the majority have suffered..</p>
  <a class="btn-light">CONTACT US</a>
</section>

<section class="services">
  <h2 class="heading section-title" style="top:902px">OUR SERVICES</h2>
  <div class="service-card" style="left:120px">
    <div class="service-photo" role="img" aria-label="Bright finished basement with white columns and a lounge area" style="background:linear-gradient(160deg,#eef0f2,#c9c4bd)"></div>
    <div class="service-label heading"><svg width="34" height="30" viewBox="0 0 34 30" fill="none" stroke="#444" stroke-width="1.5"><path d="M3 14 17 3l14 11M7 11v16h20V11"/><rect x="12" y="17" width="10" height="10"/></svg>BASEMENT REMODEL</div>
  </div>
  <div class="service-card" style="left:450px">
    <div class="service-photo" role="img" aria-label="Outdoor kitchen under a wooden pergola with stone paving" style="background:linear-gradient(160deg,#7f8f6a,#b7b3a9 55%,#6b6f68)"></div>
    <div class="service-label heading"><svg width="34" height="30" viewBox="0 0 34 30" fill="none" stroke="#444" stroke-width="1.5"><rect x="3" y="4" width="28" height="23"/><circle cx="17" cy="16" r="6"/><path d="M8 8h4M22 8h4"/></svg>OUTDOOR KITCHENS</div>
  </div>
  <div class="service-card" style="left:779px">
    <div class="service-photo" role="img" aria-label="Garden bathroom with a freestanding tub and glass shower" style="background:linear-gradient(160deg,#5d5a52,#c8c3ba 55%,#8a8478)"></div>
    <div class="service-label heading"><svg width="26" height="30" viewBox="0 0 26 30" fill="none" stroke="#444" stroke-width="1.5"><rect x="5" y="3" width="16" height="25"/><path d="M9 8h8M13 14v6"/></svg>OUTDOOR BATHROOMS</div>
  </div>
  <div class="dots" style="left:560px;top:1343px"><i></i><i class="on"></i><i></i></div>
</section>

<section class="about">
  <div class="about-photo" role="img" aria-label="Games room with a billiard table under a chandelier beside a staircase"></div>
  <div class="play"><svg width="16" height="18" viewBox="0 0 16 18"><path d="M2 1l13 8-13 8z" fill="#fff"/></svg></div>
  <h2 class="heading about-title">ABOUT HARLOW</h2>
  <p class="body-text about-text">Contrary to popular belief, Lorem Ipsum is not simply random text. It has roots in a piece of classical Latin literature from 45 BC, making it over 2000 years old. Arthur Penwell, a Latin professor at Ashford College in Westvale, looked up one of the more obscure Latin words, consectetur, from a Lorem Ipsum passage, and going through the cites of the word in classical literature, discovered the undoubtable source. Lorem Ipsum comes from sections 1.10.32 and 1.10.33 of "de Finibus Bonorum et Malorum" (The Extremes of Good and Evil) by Tullius Varro, written in 45 BC. This book is a treatise on the theory of ethics, very popular during the Renaissance.</p>
  <a class="btn-dark">READ MORE</a>
</section>

<section class="select">
  <h2 class="heading section-title" style="top:2022px">HOW TO SELECT A CONTRACTOR</h2>

  <div class="tip" style="left:148px;top:2108px">
    <svg width="72" height="64" viewBox="0 0 72 64" fill="none" stroke="#555" stroke-width="1.6"><path d="M26 4h20M26 34h20M28 4c0 12 16 12 16 15s-16 3-16 15M44 4c0 12-16 12-16 15s16 3 16 15"/><path d="M4 34l12 20 10-4M68 34 56 54l-10-4"/></svg>
    <h3 class="heading">LONGEVITY OF THE COMPANY</h3>
    <p class="body-text">Contrary to popular belief, Lorem Ipsum is not simply random text. It has roots...</p>
  </div>
  <div class="tip" style="left:473px;top:2108px">
    <svg width="72" height="64" viewBox="0 0 72 64" fill="none" stroke="#555" stroke-width="1.6"><path d="M6 60h60M12 60V14l18-10v56M30 26h18v34M48 40h14v20"/><path d="M18 20h6M18 30h6M18 40h6M36 34h6M36 44h6"/></svg>
    <h3 class="heading">WHAT OUR COMPANY DOES</h3>
    <p class="body-text">Contrary to popular belief, Lorem Ipsum is not simply random text. It has roots...</p>
  </div>
  <div class="tip" style="left:782px;top:2108px">
    <svg width="72" height="64" viewBox="0 0 72 64" fill="none" stroke="#555" stroke-width="1.6"><rect x="4" y="4" width="44" height="10"/><rect x="8" y="18" width="44" height="10"/><rect x="4" y="32" width="44" height="10"/><rect x="8" y="46" width="44" height="10"/></svg>
    <h3 class="heading">SIZE OF THE COMPANY</h3>
    <p class="body-text">Contrary to popular belief, Lorem Ipsum is not simply random text. It has roots...</p>
  </div>
  <div class="tip" style="left:148px;top:2340px">
    <svg width="72" height="64" viewBox="0 0 72 64" fill="none" stroke="#555" stroke-width="1.6"><path d="M6 4h40v56H6zM14 16h24M14 26h24M14 36h14"/><circle cx="48" cy="40" r="9"/></svg>
    <h3 class="heading">LICENSING AND PROFESSIONALISM</h3>
    <p class="body-text">Contrary to popular belief, Lorem Ipsum is not simply random text. It has roots...</p>
  </div>
  <div class="tip" style="left:473px;top:2340px">
    <svg width="72" height="64" viewBox="0 0 72 64" fill="none" stroke="#555" stroke-width="1.6"><path d="M6 34h10v24H6zM16 36l10-14c3 0 4 3 3 6l-2 6h14c3 0 4 3 2 5l-4 14H16"/><circle cx="52" cy="16" r="10"/><path d="m47 16 4 4 7-8"/></svg>
    <h3 class="heading">RECOMMENDATIONS</h3>
    <p class="body-text">Contrary to popular belief, Lorem Ipsum is not simply random text. It has roots...</p>
  </div>
  <div class="tip" style="left:782px;top:2340px">
    <svg width="72" height="64" viewBox="0 0 72 64" fill="none" stroke="#555" stroke-width="1.6"><path d="M4 26h34v22H16l-8 8v-8H4z"/><circle cx="46" cy="20" r="16"/><path d="M41 16c0-4 10-4 10 0s-5 4-5 8M46 28v1"/></svg>
    <h3 class="heading">QUESTIONS TO ASK THE CONTRACTOR</h3>
    <p class="body-text">Contrary to popular belief, Lorem Ipsum is not simply random text. It has roots...</p>
  </div>
</section>

<section class="portfolio">
  <h2 class="heading section-title" style="top:2590px">OUR PORTFOLIO</h2>
  <div class="folio" style="left:0;width:287px;background:linear-gradient(170deg,#1e2a1c,#2f8fa0 60%,#6b5a44)" role="img" aria-label="Illuminated backyard swimming pool at night"></div>
  <div class="folio" style="left:296px;width:299px;background:linear-gradient(170deg,#e9e7e2,#b9b3a9 60%,#3c3a36)" role="img" aria-label="White kitchen with an island and stainless appliances"></div>
  <div class="folio" style="left:605px;width:300px;background:linear-gradient(170deg,#56693f,#8f8b84 55%,#6e6a64)" role="img" aria-label="Stone paver patio with red outdoor sofas"></div>
  <div class="folio" style="left:913px;width:287px;background:linear-gradient(170deg,#cfcfcc,#8e8d89 60%,#5e5d5a)" role="img" aria-label="Worker laying large floor tiles"></div>
</section>

<section class="testimonials">
  <h2 class="heading section-title" style="top:3090px">TESTIMONIALS</h2>
  <div class="quote-card" style="left:88px"><span class="q">“</span><p class="body-text">Contrary to popular belief, Lorem Ipsum is not simply random text. It has roots in a piece of classical Latin literature from 45 BC,</p><h4 class="heading">DANA REYES</h4></div>
  <div class="quote-card" style="left:433px"><span class="q">“</span><p class="body-text">Contrary to popular belief, Lorem Ipsum is not simply random text. It has roots in a piece of classical Latin literature from 45 BC,</p><h4 class="heading">DANA REYES</h4></div>
  <div class="quote-card" style="left:776px"><span class="q">“</span><p class="body-text">Contrary to popular belief, Lorem Ipsum is not simply random text. It has roots in a piece of classical Latin literature from 45 BC,</p><h4 class="heading">DANA REYES</h4></div>
  <div class="avatar" style="left:114px;background:linear-gradient(160deg,#6d7f8c,#c9a58a)" role="img" aria-label="Customer portrait"></div>
  <div class="avatar" style="left:459px;background:linear-gradient(160deg,#e8eef2,#b6a08c)" role="img" aria-label="Customer portrait"></div>
  <div class="avatar" style="left:802px;background:linear-gradient(160deg,#5ca0d6,#caa68a)" role="img" aria-label="Customer portrait"></div>
  <div class="dots" style="left:588px;top:3490px"><i></i><i class="on"></i><i></i></div>
</section>

<footer>
  <div class="footer-band"></div>
  <svg class="footer-curve" viewBox="0 0 1200 300" preserveAspectRatio="none" aria-hidden="true">
    <path d="M0 0H1200V60C1000 250 260 300 0 80Z" fill="#6b6b6b"/>
    <path d="M0 0H1200V40C1000 215 280 255 0 40Z" fill="#fff"/>
  </svg>
  <h2 class="heading news-title">NEWSLETTER</h2>
  <div class="news-form"><span>Enter your email address...</span><b>SUBSCRIBE</b></div>

  <div class="foot-brand">
    <div class="mark"></div>
    <div class="name">HARLOW &amp; SONS CONSTRUCTION INC</div>
    <div class="tag">WE TREAT OUR CUSTOMERS LIKE FAMILY</div>
  </div>
  <div class="socials"><i></i><i></i><i></i><i></i></div>

  <div class="foot-col" style="left:481px"><h5>QUICK LINK</h5><ul><li>HOME</li><li>ABOUT US</li><li>SELECTING A COMPANY</li><li>OUR WORK</li><li>CONTACT US</li></ul></div>
  <div class="foot-col" style="left:670px"><h5>INFORMATION</h5><ul><li>PRIVACY POLICY</li><li>TEEMS &amp; CONDITIONS</li><li>FAQ,S</li><li>SITEMAP</li><li>BLOG</li></ul></div>
  <div class="foot-col" style="left:876px"><h5>CONTACT INFO</h5>
    <div class="contact-item"><svg width="10" height="13" viewBox="0 0 10 13"><path d="M5 0a5 5 0 00-5 5c0 4 5 8 5 8s5-4 5-8a5 5 0 00-5-5zm0 7a2 2 0 110-4 2 2 0 010 4z" fill="#fff"/></svg><span>LOCATION<br>SOME GOES ADDRESS HERE</span></div>
    <div class="contact-item"><svg width="11" height="11" viewBox="0 0 24 24"><path fill="#fff" d="M6.6 10.8a15.1 15.1 0 006.6 6.6l2.2-2.2c.3-.3.7-.4 1-.2 1.1.4 2.3.6 3.6.6.6 0 1 .4 1 1V20c0 .6-.4 1-1 1A17 17 0 013 4c0-.6.4-1 1-1h3.5c.6 0 1 .4 1 1 0 1.3.2 2.5.6 3.6.1.3 0 .7-.2 1l-2.3 2.2z"/></svg><span>PHONE<br>+00 100-555-0199</span></div>
    <div class="contact-item"><svg width="12" height="10" viewBox="0 0 12 10"><rect width="12" height="10" fill="#fff"/><path d="M0 0l6 5 6-5" fill="none" stroke="#333"/></svg><span>EMAIL<br>INFO@EXAMPLE.COM</span></div>
  </div>

  <div class="foot-rule"></div>
  <div class="to-top"><svg width="10" height="6" viewBox="0 0 10 6"><path d="M1 5l4-4 4 4" fill="none" stroke="#fff" stroke-width="1.5"/></svg></div>
  <p class="copyright">© COPYRIGHT 2023 ALL RIGHTS RESERVED</p>
</footer>

</body>
</html>
```